Business card design needed

I need a simple business card design with contact details on one side (and a logo) and 2 logos on the other side. I would like the text to be in silver and the card black.

Target Market(s)

Luxury market

Industry/Entity Type

Business

Contact Information for Business Card

M&K Forvela, PO BOX 517, Brindlecoe, VIC, 3186

Logo Text

M&K Forvela

Requirements
Must have
• black card, 2 logos on back, M&K logo on front

Text on front should be

Neil & Priya Haverstock

Neil 0417826391 Priya 0428650147
neil@mkforvela.com priya@mkforvela.com
PO BOX 517, Brindlecoe, VIC, 3186

```html
<!DOCTYPE html>
<html lang="en">
<head>
<meta charset="utf-8">
<title>M&amp;K Forvela — Business Card</title>
<link rel="stylesheet" href="https://fonts.googleapis.com/css2?family=Gelasio:wght@400&display=swap">
<style>
  :root {
    --backdrop: #2b2b2d;
    --card-white: #ffffff;
    --card-black: #221e21;
    --mark-tile: #2a2528;
    --ink-dark: #262324;
    --silver: #d6d6d8;
    --silver-soft: #b9b9bc;
  }
  * { box-sizing: border-box; margin: 0; padding: 0; }
  html, body {
    width: 1200px;
    height: 715px;
    overflow: hidden;
    background: var(--backdrop);
  }
  .canvas {
    position: relative;
    width: 1200px;
    height: 715px;
    display: flex;
    align-items: center;
    justify-content: center;
  }
  .business-card {
    display: flex;
    width: 900px;
    height: 520px;
    font-family: "Gelasio", Georgia, serif;
    box-shadow: 0 18px 40px rgba(0,0,0,0.45);
  }
  .brand-side {
    width: 430px;
    background: var(--card-white);
    display: flex;
    flex-direction: column;
    align-items: center;
    justify-content: center;
    gap: 14px;
    padding-bottom: 30px;
  }
  .brand-tile {
    width: 210px;
    height: 165px;
    border-radius: 22px;
    background: var(--mark-tile);
  }
  .brand-name {
    font-size: 32px;
    color: var(--ink-dark);
    letter-spacing: 0.5px;
  }
  .contact-side {
    flex: 1;
    background: var(--card-black);
    color: var(--silver);
    padding: 78px 0 0 70px;
  }
  .contact-person { margin-bottom: 34px; }
  .person-name {
    font-size: 33px;
    line-height: 1.15;
    color: var(--silver);
  }
  .person-line {
    font-size: 25px;
    line-height: 1.3;
    color: var(--silver-soft);
  }
  .postal-address {
    font-style: normal;
    font-size: 25px;
    line-height: 1.35;
    color: var(--silver-soft);
  }
</style>
</head>
<body>
  <main class="canvas">
    <article class="business-card">
      <section class="brand-side">
        <div class="brand-tile" aria-hidden="true"></div>
        <p class="brand-name">M&amp;K Forvela</p>
      </section>
      <section class="contact-side">
        <div class="contact-person">
          <p class="person-name">Neil Haverstock</p>
          <p class="person-line">neil@mkforvela.com</p>
          <p class="person-line">0417 826 391</p>
        </div>
        <div class="contact-person">
          <p class="person-name">Priya Haverstock</p>
          <p class="person-line">priya@mkforvela.com</p>
          <p class="person-line">0428 650 147</p>
        </div>
        <address class="postal-address">
          PO Box 517<br>
          Brindlecoe, VIC, 3186
        </address>
      </section>
    </article>
  </main>
</body>
</html>
```